Pellbry Redesign of Website

I require my webpage to look different but this is out with my current providers platform
Updates
I will benefit from designs that use my wording (this is extremely important). I appreciate there may be a lot of wording in some areas so i would be happy with "read more" in various places. The use of my face in photo is a must and my logo is also a must which can be found on m y website www.pellbryfocus.co.uk I do not want corporate feel, i would like a warm, authentic. personal and inviting feel.
5+ page

```html
<!DOCTYPE html>
<html lang="en">
<head>
<meta charset="utf-8">
<title>The Story Behind Pellbry</title>
<link href="https://fonts.googleapis.com/css2?family=Playfair+Display:wght@500;600;700&family=Montserrat:wght@400;500&family=Dancing+Script:wght@500;600&display=swap" rel="stylesheet">
<style>
:root{
  --teal:#2f6b69;
  --teal-dark:#265c5a;
  --teal-card:#3a7673;
  --heading:#2a5e5b;
  --navy:#2d3f68;
  --cream:#fbf7f1;
  --paper:#f6efe6;
  --sage:#dbe3d4;
  --mist:#e3ebec;
  --ink:#1f2a2a;
  --line:#d9d2c4;
}
*{margin:0;padding:0;box-sizing:border-box}
html,body{width:954px;height:1200px;overflow:hidden}
body{position:relative;background:var(--paper);font-family:"Montserrat",sans-serif;color:var(--ink)}
.sidebar{position:absolute;left:0;top:0;width:214px;height:1200px;background:var(--teal)}
.brand{position:absolute;left:0;top:0;width:214px;height:146px;background:var(--mist);display:flex;flex-direction:column;align-items:center;justify-content:center;gap:10px}
.brand-dot{width:42px;height:42px;border-radius:50%;background:var(--teal)}
.brand-name{font-family:"Playfair Display",serif;font-weight:600;font-size:13px;color:var(--teal);text-align:center;line-height:1.3;letter-spacing:.5px}
.nav{position:absolute;left:17px;top:185px;width:180px}
.nav-item{height:79px;margin-bottom:9.6px;border-radius:3px;background:var(--teal-card);display:flex;align-items:center;padding-left:12px;gap:9px;color:#fff;font-size:13.5px;line-height:1.4}
.nav-item svg{width:34px;height:34px;flex:none;fill:none;stroke:#e8efe9;stroke-width:1.4;stroke-linecap:round;stroke-linejoin:round}
.nav-item.active{background:var(--cream);color:var(--ink)}
.nav-item.active svg{stroke:var(--teal)}
.leaf-art{position:absolute;left:20px;top:745px;width:170px;height:440px;background:linear-gradient(200deg,rgba(170,205,190,.28),rgba(170,205,190,.05));border-radius:80px 10px 80px 10px}
.main{position:absolute;left:214px;top:0;width:740px;height:1200px}
.hero-photo{position:absolute;left:266px;top:0;width:474px;height:400px;background:linear-gradient(90deg,rgba(251,247,241,1) 0%,rgba(168,186,170,.7) 22%,#7f9b8f 45%,#5e7e63 75%,#8a9a6a 100%)}
.hero-fade{position:absolute;left:0;top:0;width:740px;height:440px;background:linear-gradient(180deg,rgba(251,247,241,0) 70%,var(--paper) 100%);pointer-events:none}
.hero-bg{position:absolute;left:0;top:0;width:740px;height:432px;background:var(--cream)}
.title{position:absolute;left:37px;top:34px;font-family:"Playfair Display",serif;font-weight:600;font-size:45px;line-height:47px;color:var(--heading)}
.subtitle{position:absolute;left:37px;top:130px;font-family:"Dancing Script",cursive;font-weight:500;font-size:25px;line-height:31px;color:var(--navy)}
.rule{position:absolute;height:1px;background:#c9cdb6}
.intro{position:absolute;left:37px;top:229px;width:250px;font-size:9.6px;line-height:14px}
.intro p{margin-bottom:5px}
.card{position:absolute;left:35px;top:369px;width:669px;height:531px;background:var(--cream);border-radius:8px}
.col{position:absolute;top:40px;width:270px}
.col h2{display:flex;align-items:center;gap:12px;font-family:"Playfair Display",serif;font-weight:600;font-size:28px;color:var(--heading);margin-bottom:12px}
.icon-circle{width:40px;height:40px;border-radius:50%;display:flex;align-items:center;justify-content:center;flex:none}
.icon-circle svg{width:22px;height:22px;fill:none;stroke:var(--heading);stroke-width:1.4;stroke-linecap:round}
.sage{background:var(--sage)}
.mist{background:#dce6e8}
.col p{font-size:9.6px;line-height:16.8px}
.col-divider{position:absolute;left:334px;top:36px;width:1px;height:117px;background:var(--line)}
.expect-title{position:absolute;left:0;top:180px;width:669px;text-align:center;font-family:"Playfair Display",serif;font-weight:600;font-size:28px;color:var(--heading)}
.grid{position:absolute;left:39px;top:232px;width:591px;display:grid;grid-template-columns:repeat(4,1fr)}
.cell{height:146px;display:flex;flex-direction:column;align-items:center;text-align:center;padding:0 10px;border-right:1px solid var(--line)}
.cell:nth-child(4n){border-right:none}
.cell:nth-child(-n+4){border-bottom:1px solid var(--line)}
.cell:nth-child(n+5){padding-top:14px}
.cell h3{font-family:"Playfair Display",serif;font-weight:600;font-size:12.5px;line-height:14.5px;color:var(--heading);margin:7px 0 5px}
.cell p{font-size:9px;line-height:13.8px}
.band{position:absolute;left:0;top:900px;width:740px;height:211px;background:linear-gradient(180deg,#f8efe4 0%,#dfe4de 45%,#9fb49f 75%,#6f8e71 100%)}
.tagline{position:absolute;left:0;top:925px;width:740px;text-align:center;font-family:"Playfair Display",serif;font-weight:600;font-size:27px;color:var(--heading)}
.tagline-sub{position:absolute;left:0;top:968px;width:740px;text-align:center;font-family:"Dancing Script",cursive;font-weight:500;font-size:22px;color:var(--navy)}
.approach{position:absolute;left:0;top:1111px;width:740px;height:89px;background:var(--paper);text-align:center}
.approach h2{font-family:"Playfair Display",serif;font-weight:600;font-size:22px;color:var(--heading);margin-top:13px;margin-bottom:6px}
.approach p{font-size:9px;line-height:14px}
</style>
</head>
<body>
<aside class="sidebar">
  <div class="brand">
    <div class="brand-dot"></div>
    <div class="brand-name">PELLBRY ADHD<br>COACHING AND WELLBEING</div>
  </div>
  <nav class="nav">
    <div class="nav-item active"><svg viewBox="0 0 34 34"><path d="M4 16 17 5l13 11"/><path d="M7 14v15h7v-9h6v9h7V14"/></svg><span>The Story<br>Behind Pellbry</span></div>
    <div class="nav-item"><svg viewBox="0 0 34 34"><circle cx="17" cy="14" r="5"/><path d="M8 28c1-5 5-8 9-8s8 3 9 8"/><circle cx="17" cy="17" r="14"/></svg><span>How Pellbry<br>Can Support You</span></div>
    <div class="nav-item"><svg viewBox="0 0 34 34"><circle cx="17" cy="17" r="13"/><circle cx="17" cy="17" r="7"/><path d="M17 4v6M17 24v6M4 17h6M24 17h6"/></svg><span>Organisation &amp;<br>Partnership</span></div>
    <div class="nav-item"><svg viewBox="0 0 34 34"><circle cx="17" cy="11" r="6"/><path d="M15 17v3h4v-3"/><path d="M3 22c5-2 10-1 14 2 4-3 9-4 14-2v8c-5-2-10-1-14 2-4-3-9-4-14-2z"/></svg><span>Resouces &amp;<br>Workbooks</span></div>
    <div class="nav-item"><svg viewBox="0 0 34 34"><rect x="9" y="11" width="22" height="15" rx="2"/><path d="m9 12 11 8 11-8"/><path d="M5 6c-2 3 0 10 5 16"/></svg><span>Contact</span></div>
    <div class="nav-item"><svg viewBox="0 0 34 34"><path d="M8 4h14l5 5v14"/><path d="M8 4v26h12"/><path d="M12 12h10M12 17h10M12 22h6"/><circle cx="25" cy="26" r="5"/><path d="m23 26 2 2 3-3"/></svg><span>Privacy Policy</span></div>
  </nav>
  <div class="leaf-art" role="img" aria-label="Faint watercolour leaf branch decoration"></div>
</aside>

<main class="main">
  <div class="hero-bg"></div>
  <div class="hero-photo" role="img" aria-label="Portrait photo of the founder smiling, seated by a mountain lake with pine forest"></div>
  <div class="hero-fade"></div>

  <h1 class="title">The Story<br>Behind Pellbry</h1>
  <p class="subtitle">Helping children, teenagers<br>and adults to thrive.</p>
  <div class="rule" style="left:37px;top:212px;width:238px"></div>

  <div class="intro">
    <p>Hi, I'm Morven Tallis, founder of Pellbry ADHD Coaching &amp; Wellbeing.</p>
    <p>I provide compassionate, neurodiversity-affirming coaching and wellbeing support for children, teenagers, adults, families and organisations.</p>
    <p>Helping people better understand themselves, build confidence and develop practical strategies for everyday life.</p>
  </div>

  <section class="card">
    <div class="col" style="left:39px">
      <h2><span class="icon-circle sage"><svg viewBox="0 0 22 22"><circle cx="11" cy="8" r="3"/><path d="M6 16c1-3 3-4 5-4s4 1 5 4"/><circle cx="11" cy="11" r="9.5" stroke-dasharray="3 2"/></svg></span>My Story</h2>
      <p>My own experience as a neurodivergent adult shaped my understanding and passion for this work. I know how challenging it can be—and how powerful the right support can be.</p>
    </div>
    <div class="col-divider"></div>
    <div class="col" style="left:367px">
      <h2><span class="icon-circle mist"><svg viewBox="0 0 22 22"><circle cx="11" cy="11" r="7"/><circle cx="11" cy="11" r="3"/><path d="M11 1v5M11 16v5M1 11h5M16 11h5"/></svg></span>My Why</h2>
      <p>I believe every neurodivergent person deserves to feel understood, valued and supported. Pellbry was created to provide practical, compassionate coaching that empowers people to thrive.</p>
    </div>

    <div class="rule" style="left:39px;top:200px;width:150px"></div>
    <div class="rule" style="left:480px;top:200px;width:150px"></div>
    <h2 class="expect-title">What You Can Expect</h2>

    <div class="grid">
      <div class="cell"><span class="icon-circle sage"><svg viewBox="0 0 22 22"><circle cx="11" cy="7" r="3"/><path d="M5 18c1-4 3-6 6-6s5 2 6 6"/></svg></span><h3>Personalised<br>Support</h3><p>Tailored coaching and counselling to suit your unique needs.</p></div>
      <div class="cell"><span class="icon-circle mist"><svg viewBox="0 0 22 22"><path d="M6 19v-4c-2-1-3-3-3-6a8 8 0 0 1 16 0l-1 5h-3v5"/></svg></span><h3>Neurodivergent<br>Affirming</h3><p>ADHD and neurodiversity expertise at the heart of everything I do.</p></div>
      <div class="cell"><span class="icon-circle sage"><svg viewBox="0 0 22 22"><circle cx="11" cy="8" r="4"/><path d="M3 12c2 3 4 6 8 7 4-1 6-4 8-7"/></svg></span><h3>Practical<br>Strategies</h3><p>Tools and techniques you can use in everyday life.</p></div>
      <div class="cell"><span class="icon-circle mist"><svg viewBox="0 0 22 22"><path d="M11 19S3 14 3 8a4 4 0 0 1 8-1 4 4 0 0 1 8 1c0 6-8 11-8 11z"/></svg></span><h3>Empathy &amp;<br>Understanding</h3><p>A safe space where you can be yourself and feel heard.</p></div>
      <div class="cell"><span class="icon-circle mist"><svg viewBox="0 0 22 22"><path d="M2 12l5-4 4 2 4-2 5 4-7 6z"/></svg></span><h3>Confidence<br>Building</h3><p>Support to build self-esteem and belief in your strengths.</p></div>
      <div class="cell"><span class="icon-circle sage"><svg viewBox="0 0 22 22"><circle cx="10" cy="12" r="7"/><circle cx="10" cy="12" r="3"/><path d="M10 12 19 3"/></svg></span><h3>Strengths<br>Focused</h3><p>We'll focus on what you're good at and build from there.</p></div>
      <div class="cell"><span class="icon-circle mist"><svg viewBox="0 0 22 22"><rect x="4" y="4" width="14" height="14" rx="1"/><path d="M7 15v-3M10 15V9M13 15v-5M16 15V7"/></svg></span><h3>Long Term<br>Growth</h3><p>Empowering you to create meaningful, lasting change.</p></div>
      <div class="cell"><span class="icon-circle sage"><svg viewBox="0 0 22 22"><circle cx="11" cy="6" r="2.5"/><path d="M11 9v10M11 13c-3 0-6-2-7-5M11 13c3 0 6-2 7-5M5 19h12"/></svg></span><h3>Holistic<br>Wellbeing</h3><p>Supporting your mind, body and emotional wellbeing together.</p></div>
    </div>
  </section>

  <div class="band" role="img" aria-label="Watercolour illustration of a mountain valley with pine trees and a river"></div>
  <p class="tagline">Your wellbeing, your journey, your way.</p>
  <p class="tagline-sub">I'm here to walk alongside you.</p>

  <section class="approach">
    <h2>The Pellbry Approach</h2>
    <p>Compassionate, practical and neurodiversity-affirming support tailored to every individual.<br>Helping people build confidence, resilience and lasting wellbeing through personalised coaching and understanding.</p>
  </section>
</main>
</body>
</html>
```